Card design for Heating and Cooling company

this is for a heating and cooling company we recently updated our logo and need to update our cards. We attached our logo so you can incorporate it into the card. We specialize in residential and commercial furnace and air condition repairs. Have been in business since 2014.

Phone number 555.284.9137

We need the following phrases
:Repairs, Installations, and maintenance
:Quality work at reasonable prices
:residential/commercial
:Licensed &Insured
:Email Pinegrovehvac47@mailbox-example.com
Name: Teodor K (Ted)
Also on back side I would like my logo with wording :Thank you for your business and refferal

Industry/Entity Type

Hvac

Contact Information for Business Card

:residential/commercial
:Licensed & Insured
Name: Teodor K (Ted)
Number:555.284.9136

Requirements
Must have
• Blue and red colors
Nice to have
• Maybe a pic of a furnace or air conditioner

```html
<!DOCTYPE html>
<html lang="en">
<head>
<meta charset="utf-8">
<title>Pinegrove Heating &amp; Cooling – Business Cards</title>
<link rel="stylesheet" href="https://fonts.googleapis.com/css2?family=Jost:wght@400;500;700&display=swap">
<style>
  :root {
    --canvas-bg: #e9e9e9;
    --card-bg: #fbfbfb;
    --ink: #1a1a1a;
    --accent-orange: #e4521f;
    --band-top: #f4f8fc;
    --band-mid: #a9cbe9;
    --band-bottom: #2277c8;
    --mark-blue: #2a9de0;
  }
  * { margin: 0; padding: 0; box-sizing: border-box; }
  html, body {
    width: 1200px;
    height: 800px;
    overflow: hidden;
    background: var(--canvas-bg);
    font-family: "Jost", sans-serif;
    color: var(--ink);
  }
  .card-sheet {
    position: relative;
    width: 1200px;
    height: 800px;
  }
  .card {
    position: absolute;
    top: 278px;
    width: 420px;
    height: 240px;
    background: var(--card-bg);
    overflow: hidden;
  }
  .card--back { left: 142px; }
  .card--front { left: 638px; display: flex; }

  /* Brand name lockup */
  .brand {
    display: flex;
    align-items: center;
    gap: 8px;
    font-weight: 700;
    color: var(--ink);
    letter-spacing: 0.5px;
  }
  .brand__dot {
    flex: none;
    border-radius: 50%;
    background: var(--mark-blue);
  }

  /* Back side */
  .card--back .brand {
    position: absolute;
    left: 0; right: 0;
    top: 92px;
    justify-content: center;
    font-size: 26px;
  }
  .card--back .brand__dot { width: 22px; height: 22px; }
  .thank-you {
    position: absolute;
    left: 0; right: 0;
    top: 192px;
    text-align: center;
    font-size: 16px;
    font-weight: 400;
  }

  /* Front side */
  .brand-band {
    width: 156px;
    height: 100%;
    background: linear-gradient(180deg, var(--band-top) 0%, var(--band-mid) 55%, var(--band-bottom) 100%);
    display: flex;
    align-items: center;
    justify-content: center;
  }
  .brand-band .brand {
    font-size: 18px;
    gap: 6px;
  }
  .brand-band .brand__dot { width: 14px; height: 14px; }
  .contact {
    padding: 42px 0 0 15px;
  }
  .contact__name {
    font-size: 21px;
    font-weight: 500;
    color: var(--accent-orange);
    line-height: 1;
    margin-bottom: 10px;
  }
  .contact__line {
    font-size: 15.5px;
    line-height: 1.2;
  }
  .services {
    list-style: none;
    margin-top: 18px;
    font-size: 13px;
    line-height: 1.3;
  }
</style>
</head>
<body>
<main class="card-sheet">
  <section class="card card--back" aria-label="Card back">
    <div class="brand"><span class="brand__dot"></span>PINEGROVE</div>
    <p class="thank-you">Thank you for your business and refferal</p>
  </section>

  <section class="card card--front" aria-label="Card front">
    <div class="brand-band">
      <div class="brand"><span class="brand__dot"></span>PINEGROVE</div>
    </div>
    <div class="contact">
      <h1 class="contact__name">Teodor K (Ted)</h1>
      <p class="contact__line">555.284.9136</p>
      <p class="contact__line">Pinegrovehvac47@mailbox-example.com</p>
      <ul class="services">
        <li>Repairs, Installations, and maintenance</li>
        <li>Quality work at reasonable prices</li>
        <li>residential/commercial</li>
        <li>Licensed &amp; Insured</li>
      </ul>
    </div>
  </section>
</main>
</body>
</html>
```